Postcard Design

We are a full service lawn maintenace and landscapig company. Everything from maintenance, fertilizer programs, to design and install.
I would like the card to have a classy look including our logo which is attached. The logo would just have to contain the lettering and the swooshes not the pine tree background if not needed.

Industry/Entity Type

It Company

```html
<!DOCTYPE html>
<html lang="en">
<head>
<meta charset="utf-8">
<title>Tall Cedar Landscaping Postcard</title>
<link rel="stylesheet" href="https://fonts.googleapis.com/css2?family=Questrial&family=Cinzel:wght@600&display=swap">
<style>
  :root {
    --page: #ffffff;
    --edge: #b9b9b9;
    --lawn-light: #a9d24a;
    --lawn-mid: #5f9a26;
    --lawn-deep: #2f5e12;
    --pine-dark: #0b1a0d;
    --pine-mid: #1f4a24;
    --pine-glow: #3f7a3c;
    --ink-white: #ffffff;
    --rule: #d4d4d4;
  }
  * { box-sizing: border-box; margin: 0; padding: 0; }
  html, body { width: 820px; height: 1200px; overflow: hidden; background: var(--page); }
  .canvas { position: relative; width: 820px; height: 1200px; }

  .card { position: absolute; left: 0; width: 820px; border: 1px solid var(--edge); overflow: hidden; }
  .card--front { top: 0; height: 591px; }
  .card--back { top: 607px; height: 593px; background: var(--page); }

  .lawn-photo {
    position: absolute; inset: 0;
    background:
      radial-gradient(ellipse 60% 40% at 55% 20%, #d8ec8a 0%, rgba(216,236,138,0) 70%),
      linear-gradient(180deg, var(--lawn-light) 0%, var(--lawn-mid) 55%, var(--lawn-deep) 100%);
  }
  .tagline {
    position: absolute; right: 30px; top: 34px; text-align: right;
    font-family: "Questrial", sans-serif; color: var(--ink-white);
    font-size: 34px; line-height: 1.5;
  }
  .tagline span { display: block; }
  .tagline .line-one { margin-right: 80px; }

  .brand-name {
    position: absolute; font-family: "Cinzel", serif; font-weight: 600;
    color: var(--ink-white); text-align: center; line-height: 1.05;
  }
  .card--front .brand-name { right: 32px; bottom: 18px; font-size: 33px; }

  .service-panel {
    position: absolute; left: 0; top: 0; width: 410px; height: 100%;
    background: radial-gradient(ellipse 80% 55% at 50% 55%, var(--pine-glow) 0%, var(--pine-mid) 45%, var(--pine-dark) 100%);
    color: var(--ink-white); text-align: center;
  }
  .service-panel .brand-name { left: 0; right: 0; top: 44px; font-size: 42px; }
  .service-list { position: absolute; left: 0; right: 0; top: 215px; list-style: none;
    font-family: "Questrial", sans-serif; font-size: 21px; }
  .service-list li { height: 38px; line-height: 38px; }
  .service-list .divider { font-size: 12px; }
  .studio-address { position: absolute; left: 0; right: 0; bottom: 28px;
    font-family: "Cinzel", serif; font-weight: 600; font-size: 20px; line-height: 1.3; }

  .stamp-box { position: absolute; left: 703px; top: 19px; width: 103px; height: 125px; border: 1px solid var(--edge); }
  .address-lines { position: absolute; left: 457px; top: 284px; width: 313px; }
  .address-lines span { display: block; height: 1px; background: var(--rule); margin-bottom: 34px; }
</style>
</head>
<body>
<main class="canvas">
  <section class="card card--front">
    <div class="lawn-photo" role="img" aria-label="Photo of children lying barefoot on a sunlit green lawn"></div>
    <p class="tagline"><span class="line-one">We will take care of your lawn</span><span>While you do what you love!</span></p>
    <p class="brand-name">Tall Cedar<br>Landscaping</p>
  </section>

  <section class="card card--back">
    <div class="service-panel">
      <p class="brand-name">Tall Cedar<br>Landscaping</p>
      <ul class="service-list">
        <li>Lawn Maintenance</li>
        <li class="divider">&#9670;</li>
        <li>Lawn designing</li>
        <li class="divider">&#9670;</li>
        <li>Landscaping</li>
        <li class="divider">&#9670;</li>
        <li>Fertilization</li>
      </ul>
      <p class="studio-address">18270 Birch Hollow<br>Ferndale, MI 48220<br>586-555-0143</p>
    </div>
    <div class="stamp-box"></div>
    <div class="address-lines"><span></span><span></span><span></span><span></span><span></span></div>
  </section>
</main>
</body>
</html>
```